IT Company needs stationary design

Business cards, MS Word, PowerPoint, A4 notepad design base on our company logo. This must be a set of templates in the same style which could be used both for printable documents as well as for documents shared digitally via email, website etc. This should be a modern design which is still professional, so make sure content is well readable both in MS Word and MS PowerPoint templates.

Target Market(s)

SME and Corporate

Industry/Entity Type

It Company

Font styles to use
Sans Serif

Colors
0455a3
0692cd
f37122
ffc214

Requirements
Must have
• 1) Business cards design: modern but still professional
• 2) MS Word: mostly for IT project documents (business analysis, reports, specifications, etc.) must be professional and easy readable.
• 3) MS PowerPoint: first slide, normal slide, last slide.
• 4) A4 notepad: header (must), footer (must), some light design on the background (optionally)
Nice to have
• Business cards design: would be nice to have 2-4 color variations of the same design from one side - cover (for example part of the cards are blue, part of the cards are orange) and other side with contact details is identical.

```html
<!DOCTYPE html>
<html lang="en">
<head>
<meta charset="utf-8">
<title>Lumenrise business card</title>
<link rel="stylesheet" href="https://fonts.googleapis.com/css2?family=Quicksand:wght@400;500&display=swap">
<style>
  :root {
    --backdrop: #d3d8d6;
    --card-white: #ffffff;
    --card-dark: #151a1a;
    --stripe-orange: #f5520f;
    --stripe-yellow: #f7b518;
    --stripe-cyan: #6fe6dc;
    --ink: #1b1b1b;
    --ink-light: #ffffff;
    --trim: #8a8f8e;
  }
  * { margin: 0; padding: 0; box-sizing: border-box; }
  html, body {
    width: 1200px; height: 720px; overflow: hidden;
    background: var(--backdrop);
    font-family: "Quicksand", "Helvetica Neue", Arial, sans-serif;
  }
  .canvas { position: relative; width: 1200px; height: 720px; }
  .card {
    position: absolute; left: 40px; top: 37px;
    width: 1120px; height: 640px;
    background: var(--card-white); overflow: hidden;
  }
  .card-shapes { position: absolute; inset: 0; width: 100%; height: 100%; }
  .trim-line {
    position: absolute; right: 0; top: 0; height: 540px;
    border-right: 1.5px dashed var(--trim);
  }
  .brand {
    position: absolute; left: 600px; top: 61px;
    display: flex; align-items: center; gap: 26px;
  }
  .brand-mark {
    width: 130px; height: 130px; border-radius: 50%;
    border: 9px solid var(--ink);
  }
  .brand-name {
    font-size: 60px; font-weight: 400; color: var(--ink);
    letter-spacing: 1px; line-height: 1;
  }
  .contact-list { position: absolute; left: 0; top: 0; width: 100%; height: 100%; list-style: none; }
  .contact-item { position: absolute; left: 0; width: 100%; }
  .contact-icon {
    position: absolute; left: 72px; width: 60px; height: 60px; fill: var(--ink-light);
  }
  .contact-text {
    position: absolute; left: 170px;
    color: var(--ink-light); font-size: 24px; font-weight: 400; line-height: 30px;
    white-space: nowrap;
  }
</style>
</head>
<body>
<div class="canvas">
  <div class="card">
    <svg class="card-shapes" viewBox="0 0 1120 640" preserveAspectRatio="none" aria-hidden="true">
      <polygon fill="var(--card-dark)" points="0,0 45,0 1120,582 1120,640 0,640"/>
      <polygon fill="var(--stripe-cyan)" points="45,0 50,0 1120,570 1120,582"/>
      <polygon fill="var(--stripe-yellow)" points="50,0 54,0 1120,558 1120,570"/>
      <polygon fill="var(--stripe-orange)" points="54,0 59,0 1120,543 1120,558"/>
    </svg>
    <div class="trim-line"></div>

    <div class="brand">
      <div class="brand-mark"></div>
      <div class="brand-name">lumenrise</div>
    </div>

    <ul class="contact-list">
      <li class="contact-item">
        <svg class="contact-icon" style="top:227px" viewBox="0 0 60 60" aria-hidden="true">
          <path d="M30 4a19 19 0 0 0-19 19c0 14 19 33 19 33s19-19 19-33A19 19 0 0 0 30 4zm0 28a9 9 0 1 1 0-18 9 9 0 0 1 0 18z"/>
          <ellipse cx="30" cy="56" rx="8" ry="2.5"/>
        </svg>
        <p class="contact-text" style="top:230px">1111,example, XXXX<br>US, XXXXX</p>
      </li>
      <li class="contact-item">
        <svg class="contact-icon" style="top:325px" viewBox="0 0 60 60" aria-hidden="true">
          <path d="M16 6l9 11-5 6c3 7 9 13 16 16l6-5 11 9-6 9C27 50 10 33 8 12z"/>
        </svg>
        <p class="contact-text" style="top:343px">XXX-XXX-XXXX</p>
      </li>
      <li class="contact-item">
        <svg class="contact-icon" style="top:412px" viewBox="0 0 60 60" aria-hidden="true">
          <path d="M3 12h54L30 34z"/>
          <path d="M3 17l27 22 27-22v31H3z"/>
        </svg>
        <p class="contact-text" style="top:423px">email@example.com</p>
      </li>
      <li class="contact-item">
        <svg class="contact-icon" style="top:503px" viewBox="0 0 60 60" aria-hidden="true">
          <path d="M3 4h54v38H3zm6 6v26h42V10z"/>
          <rect x="26" y="42" width="8" height="7"/>
          <path d="M16 56c0-5 6-7 14-7s14 2 14 7z"/>
        </svg>
        <p class="contact-text" style="top:510px">www.example.com</p>
      </li>
    </ul>
  </div>
</div>
</body>
</html>
```